December online webinar for our coaching and mentoring business.

needing an email flyer and something to use on appropriate social media e.g. Instagram to promote our December half day webinar focusing on positive mindset, relationships and 2021 being a new year with new opportunities. For the feel of what we have done previously:
www.qlvgetaways.com.au
We will be using 2 guest speakers:
Dominic Farrow of 60Quests.com and
Marisa Holt, psychologist and both will need to be prominent on the marketing material we send out on email and use on social media.
The webinar will likely run Thursday December 10th from 12.30pm to 4.30pm AEST and will be hosted and facilitated by me and on behalf of Portwell Business Coaching.
I am thinking colour schemes and branding similar to what you see on the website above.
Pricing needs to be on the flyer - $750 + GST per person*
*enquire for multi booking discounts for 2 people or more

Target Market(s)

people looking for a boost before the year end and a fast start to 2021

Font styles to use
Sans Serif

Requirements
Must have
• see brief above
Nice to have
• see brief above
Should not have
• see brief above

```html
<!DOCTYPE html>
<html lang="en">
<head>
<meta charset="utf-8">
<title>Sprint Finish to 2020 – Portwell Business Coaching Webinar</title>
<link rel="stylesheet" href="https://fonts.googleapis.com/css2?family=Arimo:wght@400;700&family=Bebas+Neue&display=swap">
<style>
  :root {
    --red: #e8393a;
    --charcoal: #3d3d40;
    --ink: #3a3a3a;
    --body: #4a4a4a;
    --white: #ffffff;
    --black: #111111;
  }
  * { margin: 0; padding: 0; box-sizing: border-box; }
  html, body { width: 1200px; height: 2722px; overflow: hidden; background: var(--white); }
  body { position: relative; font-family: "Arimo", Arial, sans-serif; }

  .hero { position: absolute; left: 0; top: 0; width: 1200px; height: 512px; overflow: hidden; }
  .hero-photo { position: absolute; inset: 0;
    background: linear-gradient(135deg, #2b2624 0%, #4a3a30 38%, #7a5d45 60%, #b9b6b4 78%, #8d7058 100%); }
  .hero-shade { position: absolute; left: 0; top: 0; width: 520px; height: 512px;
    background: linear-gradient(90deg, rgba(40,40,42,.75), rgba(40,40,42,0)); }
  .brand { position: absolute; left: 42px; top: 52px; color: var(--red); font-weight: 700;
    font-size: 26px; letter-spacing: .5px; }
  .headline { position: absolute; left: 42px; top: 190px; color: var(--white); font-weight: 700;
    font-size: 53px; line-height: 1.0; }
  .headline-box { position: absolute; left: 0; top: 316px; width: 450px; height: 144px;
    background: var(--red); padding: 17px 0 0 42px; color: var(--white); font-weight: 700;
    font-size: 53px; line-height: 1.0; }

  .intro { position: absolute; left: 0; top: 512px; width: 1200px; height: 547px;
    background: var(--charcoal); padding: 50px 54px 0 52px; color: var(--white); }
  .intro p { font-size: 24.6px; line-height: 30.6px; text-align: justify; margin-bottom: 31px; }

  .section-title { position: absolute; left: 50px; top: 1106px; color: var(--red);
    font-family: "Bebas Neue", "Arimo", sans-serif; font-size: 58px; line-height: 1; }

  .speaker-name { position: absolute; left: 364px; color: var(--ink); font-weight: 700;
    font-size: 27px; letter-spacing: .3px; }
  .speaker-bio { position: absolute; left: 364px; width: 782px; color: var(--body); }
  .speaker-bio p { font-size: 19.2px; line-height: 31px; text-align: justify; margin-bottom: 31px; }
  .speaker-photo { position: absolute; left: 51px; width: 276px; }
  .photo-mono { background: linear-gradient(180deg, #cfcfcf 0%, #6b6b6b 45%, #1c1c1c 100%); }
  .photo-colour { background: linear-gradient(160deg, #f1d27a 0%, #d8b26a 35%, #3d7aa3 70%, #1f4f76 100%); }

  .event { position: absolute; left: 45px; top: 2349px; width: 1100px; height: 338px;
    background: var(--red); text-align: center; }
  .event-date { font-family: "Bebas Neue", "Arimo", sans-serif; color: var(--white);
    font-size: 58px; line-height: 1; margin-top: 42px; }
  .event-price { font-family: "Bebas Neue", "Arimo", sans-serif; color: var(--black);
    font-size: 36px; line-height: 44px; margin-top: 36px; }
  .event-contacts { display: flex; justify-content: space-between; padding: 0 22px;
    margin-top: 34px; color: var(--white); font-weight: 700; font-size: 27px; }
</style>
</head>
<body>

<header class="hero">
  <div class="hero-photo" role="img" aria-label="Desk scene with a branded spiral notebook, a pen and a striped mug on wooden tabletop"></div>
  <div class="hero-shade"></div>
  <div class="brand">Portwell Business Coaching</div>
  <h1 class="headline">SPRINT FINISH<br>TO 2020.</h1>
  <div class="headline-box">FAST START<br>TO 2021.</div>
</header>

<section class="intro">
  <p>Most of us cannot wait to see the back of 2020 and whilst it has presented us with totally unprecedented challenges and struggles, there is also opportunity. Some have not only survived these past 8 months but veritably thrived in the environment. We have an opportunity to look forward, plan what we can and focus on what we can control.</p>
  <p>To set us up for a sprint finish to the year and a fast start to 2021 I will be your host for a half day webinar focused on inspiring your thinking and helping you get focused on what's important. Marisa Holt and Dominic Farrow will be sharing their thoughts on what we all need right now and presenting practical and simple ways in which to channel our energies and getting us set for a strong finish to this weird year and the fastest of starts to the next one.</p>
  <p>To reserve your place at what is sure to be an inspirational and motivational workshop-syle session just reply to this email and we look forward to seeing you there. We are limiting places to ensure we retain a degree of intimacy and engagement to the webinar so don't wait until the last minute to get in touch and book your place!</p>
</section>

<h2 class="section-title">GUEST SPEAKERS</h2>

<h3 class="speaker-name" style="top:1187px;">DOMINIC FARROW</h3>
<div class="speaker-photo photo-mono" style="top:1314px;height:278px;" role="img" aria-label="Black and white portrait of guest speaker Dominic Farrow"></div>
<div class="speaker-bio" style="top:1245px;">
  <p>After the loss of a close friend in his early twenties, Dominic penned down a list of 60 quests that he hoped would bring him closer to a sense of happiness. Now 10 years on and counting, Dom has ticked off 44 items from his list, has raised almost half a million dollars for charities and has found a sense of purpose that he could never have dreamed of.</p>
  <p>His story turned into books, TV shows and documentaries, has most impressively inspired a global community of individuals and organizations who have identified, pursued, and achieved their own goals, too.</p>
  <p>Guaranteed to make you laugh, cry and ignite your imagination, Dominic's talks are like no other. They create an environment for thinking, education and change providing the audience with a toolkit to engage, connect and inspire. You will leave with a different outlook and a renewed energy and motivation to create your own list and plan for a positively different future</p>
</div>

<h3 class="speaker-name" style="top:1756px;left:362px;">MARISA HOLT</h3>
<div class="speaker-photo photo-colour" style="top:1889px;height:306px;" role="img" aria-label="Colour portrait of guest speaker Marisa Holt"></div>
<div class="speaker-bio" style="top:1815px;left:362px;">
  <p>Marisa will discuss how to create thriving relationships, personally and professionally. As social creatures, we desire meaningful connections with others and a sense of acceptance and belonging within our personal and professional tribes. When we feel disharmony or experience pressures within our relationships, our well-being and capacity to thrive are impacted both at home and at work. While relationship challenges have existed since the dawn of time, sharing love and life with others during COVID has placed many relationships under additional pressures, while others have reconnected and found joy perhaps due to the slower pace of life, and the fewer distractions lockdown has brought with it.</p>
  <p>Marisa is a psychologist and speaker who works in the areas of relationships, wellbeing, career development and leadership. She is the resident psychologist and social commentator on the top rating ‘Afternoons’ program at Radio 4KT, Ambassador and Resident Psychologist with HIREWAY, and the co-host on new conversations podcast, Everyday Gears, which shares the real, raw, and very human stories of extraordinary ordinaries.</p>
</div>

<section class="event">
  <div class="event-date">THURSDAY, DECEMBER 10TH FROM 12.30PM TO 4.30PM AEST</div>
  <div class="event-price">$750 + GST PER PERSON + DISCOUNTS AVAILABLE<br>FOR GROUP AND BUSINESS BOOKINGS OF 2 PEOPLE OR MORE.</div>
  <div class="event-contacts">
    <span>www.portwell.com.au</span>
    <span>www.qlvgetaways.com.au</span>
    <span>leon@portwell.com.au</span>
  </div>
</section>

</body>
</html>
```